Local Newspaper Quarterly " Meet The Realtor" print ad

I need a new add made up. This was my last ad:
http://www.heraldpostlistings.example/static/pdfs/agents1309/Ar092213%20G10%20006%20Prepress.pdf

I do not really care of Realtor advertisements because they are just so cheesy and rather pompous-like. However, it's a necessary evil
My ads have always been outside of the box and/or visually sharp.
I now have a new company' Vorel Real Estate( I will attach a logo) contact info:
Cale Vorel
Vorel Real Estate
Broker/Owner( this can be somewhere in small print or corner of ad since it's mandatory to have shown
Phone: 304-555-0147
Email: Cale@VorelRealEstate.Example
VorelRealEstate.Example
I would like social icons(FB,Twitter, Pinterest! Houzz, Gplus)

Ideas: In my logo font or using the image at the top I envision
Something like:
A
Vorel Real Estate
Of Mind
Body of ad?
Images of Charleston WV as a real light back ground
With 3 or 4 customer reviews chosen by you in this site:
http://webcale.example/think.html

Bottom: contact info and my name in a nice Signature style ??
My agent pic at the bottom right( to be small. I don't want my big head overshadowing the message)

I have yet to think of a tagline for my new company:
I have been thinking of " Luxury Services For All Things Real Estate"

Or nothing at all ??? I don't care for tag lines but then again that's part of the business

Target Market(s)

Higher end homes

Industry/Entity Type

Business

Colors
0f59a5
0392cd
0f0f0f
eaeaea
ffffff

Requirements
Must have
• My logo and colors
Nice to have
• My agent picture and client review.
Should not have
• No typical real estate images like a house or home buyer

```html
<!DOCTYPE html>
<html lang="en">
<head>
<meta charset="utf-8">
<title>Vorel Real Estate – Meet The Realtor</title>
<link rel="stylesheet" href="https://fonts.googleapis.com/css2?family=League+Gothic&family=Aleo:ital,wght@0,400;1,400;1,700&display=swap">
<style>
  :root {
    --brand-navy: #0f59a5;
    --brand-blue: #0392cd;
    --brand-sky: #00a8e8;
    --ink: #0f0f0f;
    --mist: #eaeaea;
    --paper: #ffffff;
  }
  * { margin: 0; padding: 0; box-sizing: border-box; }
  html, body { width: 848px; height: 1200px; overflow: hidden; background: var(--paper); }
  .ad {
    position: relative;
    width: 848px;
    height: 1200px;
    overflow: hidden;
    background: linear-gradient(180deg, var(--paper) 0%, var(--paper) 58%, #f1f1f1 72%, #cfcfcf 94%, #e4e4e4 100%);
    font-family: "Aleo", Georgia, serif;
    color: var(--ink);
  }
  .hero {
    position: absolute;
    left: 0; top: 0;
    width: 848px; height: 515px;
    background: linear-gradient(160deg, #1a1a1a 0%, #6f6f6f 22%, #d4d4d4 42%, #bdbdbd 55%, #7a7a7a 72%, #2d2d2d 100%);
  }
  .hero-mark {
    position: absolute;
    left: 404px; top: 104px;
    width: 40px; height: 40px;
    border-radius: 50%;
    background: var(--brand-blue);
  }
  .hero-name {
    position: absolute;
    left: 0; top: 160px;
    width: 848px;
    text-align: center;
    font-family: "League Gothic", "Arial Narrow", sans-serif;
    font-size: 110px;
    line-height: 1;
    letter-spacing: 4px;
    color: var(--paper);
    text-transform: uppercase;
  }
  .headline {
    position: absolute;
    left: 0; width: 848px;
    text-align: center;
    white-space: nowrap;
    font-family: "League Gothic", "Arial Narrow", sans-serif;
    font-weight: 400;
    text-transform: uppercase;
    line-height: 1;
    text-shadow: 0 0 6px rgba(3,146,205,.35);
  }
  .headline--tagline { top: 536px; left: 22px; font-size: 56px; color: var(--brand-navy); }
  .headline--reviews { top: 741px; left: -26px; font-size: 54px; color: var(--brand-blue); }
  .intro {
    position: absolute;
    left: 34px; top: 623px; width: 780px;
    text-align: center;
    font-style: italic;
    font-size: 13.3px;
    line-height: 17px;
  }
  .review {
    position: absolute;
    left: 26px; width: 796px;
    text-align: center;
    font-size: 13.8px;
    line-height: 17px;
  }
  .review--first { top: 795px; }
  .review--second { top: 897px; }
  .review-author { display: block; font-style: italic; font-weight: 700; font-size: 13px; }
  .contact-card {
    position: absolute;
    left: 275px; top: 1026px;
    width: 420px; height: 120px;
    border-radius: 60px 0 0 60px;
    background: var(--brand-sky);
  }
  .contact-lines {
    position: absolute;
    left: 296px; top: 1032px; width: 340px;
    text-align: center;
    font-style: italic;
    font-size: 13.2px;
    line-height: 17px;
    color: #1d2a36;
  }
  .agent-photo {
    position: absolute;
    left: 627px; top: 981px;
    width: 196px; height: 196px;
    border-radius: 50%;
    border: 5px solid var(--paper);
    box-shadow: 0 2px 6px rgba(0,0,0,.35);
    background: radial-gradient(circle at 50% 45%, #c9a184 0%, #8b6a3c 45%, #4d5a2c 100%);
  }
  .social-row { position: absolute; left: 13px; top: 1136px; }
</style>
</head>
<body>
<main class="ad">
  <div class="hero" role="img" aria-label="Brushed steel backdrop with the company name shown in dimensional lettering"></div>
  <div class="hero-mark"></div>
  <div class="hero-name">Vorel Real Estate</div>

  <h1 class="headline headline--tagline">The complex world of real estate made simple</h1>

  <p class="intro">Lorem ipsum dolor sit amet, consectetur adipisicing elit, sed do eiusmod tempor incididunt ut labore et dolore magna aliqua. Ut enim ad minim veniam, quis nostrud exercitation ullamco laboris nisi ut aliquip ex ea commodo consequat. Duis aute irure dolor in reprehenderit in voluptate velit esse cillum dolore eu fugiat nulla pariatur. Excepteur sint occaecat cupidatat non proident, sunt in culpa qui officia deserunt mollit anim id est laborum.</p>

  <h2 class="headline headline--reviews">The voice of our customers</h2>

  <blockquote class="review review--first">
    Cale Vorel is an amazing Realtor. He made our experience as first-time home buyers very easy to understand and he took a real hands on approach. He went out of his way to be available to my family and was wonderful to our children. Cale is great at his job and I wish him only the best in his future with Summit Crest Realty.
    <cite class="review-author">~Marco and Dana Ellery~</cite>
  </blockquote>

  <blockquote class="review review--second">
    Mr.Vorel was exceptionally professional in every aspect of serving our real estate needs. His attitude, initiative and attentiveness was nothing less than outstanding. This is our fourth home purchase and Mr.Vorel’s service was “head and shoulders” above anything we have experienced in the past. We would highly recommend Mr.Vorel to any prospective client in the future.
    <cite class="review-author">~Grant and Lena Hollis~</cite>
  </blockquote>

  <div class="contact-card"></div>
  <address class="contact-lines">
    Cale Vorel<br>
    Vorel Real Estate<br>
    Broker/Owner<br>
    Phone: 304-555-0147<br>
    Email: Cale@VorelRealEstate.Example<br>
    VorelRealEstate.Example
  </address>

  <div class="agent-photo" role="img" aria-label="Agent portrait photo against autumn foliage"></div>

  <svg class="social-row" width="240" height="54" viewBox="0 0 240 54" aria-label="Social links">
    <g fill="#ffffff" stroke="#9a9a9a" stroke-width="1">
      <circle cx="26" cy="27" r="25"/>
      <circle cx="87" cy="27" r="25"/>
      <circle cx="148" cy="27" r="25"/>
      <circle cx="209" cy="27" r="25"/>
    </g>
  </svg>
</main>
</body>
</html>
```